Flyer für Mobile Massage am Arbeitsplatz
Zielgruppe
Der Flyer richtet sich an Geschäftsleitungen, Firmenvorstände, Betriebsräte.
Ich werde den Flyer sowohl persönlich überreichen, als auch postalisch verschicken.
Aufgabenstellung
Es geht um einen Flyer, DIN lang, Hochformat, beidseitig bedruckt.

```html
<!DOCTYPE html>
<html lang="de">
<head>
<meta charset="utf-8">
<title>Mobile Massage am Arbeitsplatz – Flyer</title>
<link href="https://fonts.googleapis.com/css2?family=Arimo:wght@400;700&display=swap" rel="stylesheet">
<style>
:root{
  --stage:#2b3a55;
  --paper:#ffffff;
  --paper-shade:#eceef1;
  --ink:#1c2a4a;
  --text:#2a2f3a;
  --accent:#2a5db8;
  --frame:#9aa0a8;
  --footer:#d4d7dc;
  --footer-text:#555c66;
  --photo-warm:#b59a6a;
  --photo-warm-light:#d2bb8a;
  --photo-cool:#8e98a4;
  --photo-cool-light:#b8bfc7;
}
*{margin:0;padding:0;box-sizing:border-box}
html,body{width:1200px;height:899px;overflow:hidden;background:var(--stage)}
body{font-family:"Arimo",Arial,sans-serif;position:relative}
.panel{
  position:absolute;top:50px;width:380px;height:800px;
  background:linear-gradient(160deg,var(--paper) 0%,var(--paper-shade) 100%);
  overflow:hidden;box-shadow:0 6px 24px rgba(0,0,0,.35);
}
.panel--front{left:170px}
.panel--back{left:650px}
.footer{
  position:absolute;left:0;right:0;bottom:0;height:44px;background:var(--footer);
  display:flex;align-items:center;justify-content:center;
  font-size:13px;color:var(--footer-text);letter-spacing:.2px;
}
.title{position:absolute;left:70px;top:48px;color:var(--ink)}
.title h1{font-size:33px;font-weight:700;line-height:1}
.title p{font-size:19px;margin-top:14px;margin-left:2px}
.photo{position:absolute;border:4px solid var(--frame);border-radius:4px}
.photo--warm{background:linear-gradient(150deg,var(--photo-warm-light),var(--photo-warm))}
.photo--cool{background:linear-gradient(150deg,var(--photo-cool-light),var(--photo-cool))}
.photo--plain{border:none;border-radius:2px}
.phone{position:absolute;left:36px;bottom:86px;font-size:19px;color:var(--ink)}
.copy{
  position:absolute;right:26px;top:60px;width:300px;text-align:right;
  font-size:13px;line-height:1.3;color:var(--text);
}
.copy p{margin-bottom:12px}
.hl{color:var(--accent)}
.copy .stack{width:150px;margin-left:auto}
.prices{position:absolute;right:26px;bottom:62px;text-align:right;font-size:13px;line-height:1.3;color:var(--text)}
</style>
</head>
<body>

<section class="panel panel--front">
  <div class="title"><h1>Mobile Massage</h1><p>am Arbeitsplatz</p></div>
  <div class="photo photo--warm" style="left:26px;top:190px;width:200px;height:220px" role="img" aria-label="Foto: Masseur behandelt einen Mann auf einem Massagestuhl"></div>
  <div class="photo photo--warm" style="left:240px;top:188px;width:112px;height:112px" role="img" aria-label="Foto: Nackenmassage im Büro"></div>
  <div class="photo photo--cool" style="left:240px;top:312px;width:112px;height:110px" role="img" aria-label="Foto: Rückenmassage auf dem Massagestuhl"></div>
  <div class="photo photo--cool" style="left:26px;top:424px;width:100px;height:140px" role="img" aria-label="Foto: Massage am Arbeitsplatz"></div>
  <div class="photo photo--warm" style="left:140px;top:436px;width:112px;height:128px" role="img" aria-label="Foto: Armmassage auf dem Massagestuhl"></div>
  <div class="phone">Tel.: 030-48213906</div>
  <div class="footer">www.mobile-massage-spreeland.de</div>
</section>

<section class="panel panel--back">
  <div class="copy">
    <p>In unseren Massagen am Arbeitsplatz lassen wir Elemente aus der <span class="hl">Shiatsu - Energiemassage</span> und den <span class="hl">Joint Release - Gelenklockerungen</span> zusammenfließen.</p>
    <p>Auf diese Weise eröffnen wir einen Raum für spürbare <span class="hl">Entspannung mitten im Arbeitsalltag.</span></p>
    <p class="stack">Die Massagen befreien aus berufsbedingten Zwangshaltungen, wirken stressmindernd und stimmungshebend im Team. Sie konzentrieren sich auf die Problemzonen im Rücken, Nacken, Schulter und Mausarm und sind ein Baustein im innerbetrieblichen Gesundheitsmanagement.</p>
    <p class="stack">Die Kosten können, sofern vom Arbeitgeber getragen, nach §3 Nr. 34 EStG von der Steuer abgesetzt werden.</p>
  </div>
  <div class="photo photo--cool photo--plain" style="left:30px;top:300px;width:160px;height:250px" role="img" aria-label="Foto: Masseur behandelt den Rücken eines Mannes auf dem Massagestuhl"></div>
  <div class="prices"><span class="hl">Preise:</span><br>20 Minuten : 15 Euro<br>inklusive Anfahrt<br>buchbar ab 4 Personen</div>
  <div class="footer">www.mobile-massage-spreeland.de</div>
</section>

</body>
</html>
```